New Managed IT company needs a business card

We are an IT management and support company that needs a business card design. I have a logo that I'll provide. Blues and blacks match the logo, but i'm open to anything. I want the card to help people take us seriously, but still have some energy and fun in it. The card should communicate stability and a solid company.

Target Market(s)

Target market includes Owners and Presidents at small businesses of 20 - 100 employees in the Pittsburgh PA area.

Industry/Entity Type

Information Technology

Contact Information for Business Card

i am open to other designs, but i imagine having only the logo on one side and then the logo plus all contact details on the other side.

Requirements
Must have
• Our logo
• Company name is optional if the logo makes it obvious
• A name - Cole Perrin
• A title - President
• A phone number - 724-XXX-XXXX
• A mobile phone number - 724-615-2748
• An email address - cperrin@techvaultgrid.com
• a website - techvaultgrid.com or www.techvaultgrid.com
Nice to have
• some people tell me the logo feels like a superhero theme, some fun with that idea might be good. I'm open to ideas.
Should not have
• stock photos of people or computers - especially old looking stuff.

```html
<!DOCTYPE html>
<html lang="en">
<head>
<meta charset="utf-8">
<title>TechVault Grid — Business Card</title>
<link rel="stylesheet" href="https://fonts.googleapis.com/css2?family=Roboto:wght@400;500;700&display=swap">
<style>
  :root {
    --bg: #4a413c;
    --card: #151617;
    --card-edge: #222426;
    --blue: #1f6fc0;
    --blue-bright: #2a86d8;
    --white: #f2f3f4;
    --silver: #b9bcbf;
    --grey: #8d9094;
    --divider: #5a5d61;
  }
  * { margin: 0; padding: 0; box-sizing: border-box; }
  html, body { width: 1200px; height: 864px; overflow: hidden; }
  body {
    background: var(--bg);
    font-family: "Roboto", Arial, sans-serif;
    position: relative;
  }
  .card {
    position: absolute;
    top: 281px;
    width: 530px;
    height: 302px;
    background: var(--card);
    border: 1px solid var(--card-edge);
    border-radius: 4px;
    box-shadow: 0 14px 30px rgba(0,0,0,.45);
  }
  .card--front { left: 50px; }
  .card--back { left: 620px; }

  .brand { display: flex; align-items: center; gap: 12px; }
  .brand__dot {
    border-radius: 50%;
    background: var(--blue);
    flex: none;
  }
  .brand__name {
    font-weight: 700;
    letter-spacing: 2px;
    text-transform: uppercase;
    color: var(--silver);
  }

  /* front */
  .card--front .front__content {
    position: absolute; inset: 0;
    display: flex; flex-direction: column;
    align-items: center; justify-content: center; gap: 26px;
  }
  .card--front .brand__dot { width: 44px; height: 44px; }
  .card--front .brand__name { font-size: 30px; }
  .front__web {
    font-size: 14px; letter-spacing: 4px; color: var(--grey);
  }

  /* back */
  .back__brand {
    position: absolute; left: 30px; top: 0; bottom: 0;
    width: 220px; display: flex; align-items: center;
  }
  .card--back .brand { gap: 9px; }
  .card--back .brand__dot { width: 30px; height: 30px; }
  .card--back .brand__name { font-size: 19px; color: var(--white); letter-spacing: 1.5px; }
  .back__divider {
    position: absolute; left: 262px; top: 50px; bottom: 70px;
    width: 1px; background: var(--divider);
  }
  .contact {
    position: absolute; left: 288px; top: 88px;
  }
  .contact__name { color: var(--blue-bright); font-size: 21px; font-weight: 500; }
  .contact__title { color: var(--white); font-size: 15px; margin: 2px 0 18px; }
  .contact__list { list-style: none; }
  .contact__item {
    display: flex; align-items: center; gap: 9px;
    color: var(--white); font-size: 13.5px; line-height: 22px;
  }
  .contact__icon { width: 13px; height: 13px; fill: var(--blue-bright); flex: none; }
</style>
</head>
<body>
  <section class="card card--front" aria-label="Card front">
    <div class="front__content">
      <div class="brand">
        <span class="brand__dot"></span>
        <span class="brand__name">TechVault Grid</span>
      </div>
      <p class="front__web">www.techvaultgrid.com</p>
    </div>
  </section>

  <section class="card card--back" aria-label="Card back">
    <div class="back__brand">
      <div class="brand">
        <span class="brand__dot"></span>
        <span class="brand__name">TechVault Grid</span>
      </div>
    </div>
    <div class="back__divider"></div>
    <div class="contact">
      <p class="contact__name">Cole Perrin</p>
      <p class="contact__title">President</p>
      <ul class="contact__list">
        <li class="contact__item">
          <svg class="contact__icon" viewBox="0 0 16 16"><path d="M1 5c0-2 2-3 3-3l1 3-2 1c1 2 3 4 5 5l1-2 3 1c0 1-1 3-3 3C5 13 1 9 1 5z"/></svg>
          724-390-5164
        </li>
        <li class="contact__item">
          <svg class="contact__icon" viewBox="0 0 16 16"><path d="M4 0h8v16H4zM5.5 2v10h5V2z"/></svg>
          724-615-2748
        </li>
        <li class="contact__item">
          <svg class="contact__icon" viewBox="0 0 16 16"><path d="M0 3h16v10H0zM1.5 4.5v.6L8 9l6.5-3.9v-.6z"/></svg>
          cperrin@techvaultgrid.com
        </li>
        <li class="contact__item">
          <svg class="contact__icon" viewBox="0 0 16 16"><circle cx="8" cy="8" r="7"/></svg>
          www.techvaultgrid.com
        </li>
      </ul>
    </div>
  </section>
</body>
</html>
```